Need Business Card Design, Letterhead and a Basic Form layout based on Existing Logo

We need (1) a business card design, (2) a letterhead design and (3) a basic form layout for an international holding company. This holding company has just formed two (2) sub-companies. The logo is the same for each company with only a simple word change for each company. The business card, letterhead and form design will be essentially the same for each company... with only the one word change being different.
The names of the companies are as follows:
1. Kestrel Trust Services
2. Kestrel Immigration Services
The design for the business card, letterhead and Form must be strong, clean and classy.
Our clients will be older, wealthy and mostly Asian. The design must project strength, stability and confidence.
The card may contain the following data:
1. The Logo
2. The name of the person
3. The title of the person
4. The address of the company
5. The Company Phone number
6. The personal mobile number
7. The Skype number (VOIP)
8. The WICKR number (IM)
9. The email
10. The website
We will attach AI files of our logo for the "Kestrel Trust Services" company in the colors Black/White and Blue in both Horizontal and Vertical format... We have also included separate files of the logo icon.
We uploaded the AI files to give the designer the maximum options regarding color and effects. We included the separate files for the icon because we would like to give the designer the option of a watermark. Also, we think it might be nice to highlight the icon on the back of the card perhaps with the website address.
We are not sure which colors or color combinations would be best for these two companies. We know the colors must again project strength, stability and confidence. Perhaps, a combination that might include Tan, Black and White... not sure... need design help... remember this has to have the presence of a bank-like institution... no cartoonish designs or flashy color combinations... please.
The basic form layout will be used for various questionaires, input sheets and instructions.... etc.
NOTE: The fonts used in the logo are Trajan Pro Bold for word "KESTREL" and Trajan Pro Regular for "XXXXXXXXX SERVICES".

```html
<!DOCTYPE html>
<html lang="en">
<head>
<meta charset="utf-8">
<title>Kestrel Trust Services — Stationery</title>
<link rel="stylesheet" href="https://fonts.googleapis.com/css2?family=Cinzel:wght@400;600&family=Lato:wght@400&display=swap">
<style>
  :root {
    --stage: #2e2e2e;
    --paper: #ffffff;
    --brown-deep: #2f1c12;
    --brown-mid: #5b3b27;
    --brown-ink: #4a2e1e;
    --tan-light: #e2d7cc;
    --watermark: #ede8e4;
  }
  html, body {
    margin: 0;
    padding: 0;
    width: 1200px;
    height: 1142px;
    overflow: hidden;
    background: var(--stage);
  }
  .canvas {
    position: relative;
    width: 1200px;
    height: 1142px;
  }
  .brand-square { display: block; }

  /* Presentation folder / form sheet */
  .folder {
    position: absolute;
    left: 40px;
    top: 60px;
    width: 500px;
    height: 800px;
    background: var(--paper);
    overflow: hidden;
  }
  .folder__corner {
    position: absolute;
    top: 0;
    right: 0;
    width: 120px;
    height: 120px;
    background: linear-gradient(135deg, var(--brown-mid) 0%, var(--brown-deep) 100%);
    clip-path: polygon(0 0, 100% 0, 100% 100%);
  }
  .folder__corner .brand-square {
    position: absolute;
    top: 22px;
    right: 22px;
    width: 26px;
    height: 26px;
    background: var(--tan-light);
    opacity: 0.85;
  }

  /* Letterhead */
  .letterhead {
    position: absolute;
    left: 560px;
    top: 60px;
    width: 600px;
    height: 800px;
    background: var(--paper);
  }
  .letterhead__brand {
    position: absolute;
    top: 56px;
    left: 0;
    right: 0;
    text-align: center;
    color: var(--brown-ink);
    font-family: "Cinzel", serif;
    font-weight: 600;
  }
  .letterhead__brand .brand-square {
    margin: 0 auto 12px;
    width: 32px;
    height: 32px;
    background: var(--brown-ink);
  }
  .letterhead__brand .brand-name {
    display: block;
    font-size: 26px;
    letter-spacing: 1px;
    line-height: 1;
  }
  .letterhead__brand .brand-sub {
    display: block;
    font-size: 14px;
    letter-spacing: 0.5px;
    margin-top: 4px;
  }
  .letterhead__watermark {
    position: absolute;
    top: 360px;
    left: 0;
    right: 0;
    text-align: center;
    font-family: "Cinzel", serif;
    font-weight: 600;
    font-size: 84px;
    letter-spacing: 4px;
    color: var(--watermark);
  }
  .letterhead__footer {
    position: absolute;
    bottom: 40px;
    left: 0;
    right: 0;
    text-align: center;
    font-family: "Lato", sans-serif;
    font-size: 10.5px;
    letter-spacing: 0.2px;
    color: var(--brown-ink);
  }

  /* Business cards */
  .card {
    position: absolute;
    top: 896px;
    width: 360px;
    height: 206px;
    background: radial-gradient(ellipse at 50% 45%, var(--brown-mid) 0%, var(--brown-deep) 85%);
    color: var(--tan-light);
    box-sizing: border-box;
  }
  .card--back {
    left: 40px;
    text-align: center;
  }
  .card--back .brand-square {
    width: 44px;
    height: 44px;
    margin: 46px auto 14px;
    background: var(--tan-light);
    opacity: 0.85;
  }
  .card--back .brand-name {
    display: block;
    font-family: "Cinzel", serif;
    font-weight: 600;
    font-size: 16px;
    letter-spacing: 2px;
  }
  .card__web {
    position: absolute;
    bottom: 30px;
    left: 0;
    right: 0;
    font-family: "Lato", sans-serif;
    font-size: 10px;
    letter-spacing: 1.2px;
  }
  .card--front {
    left: 420px;
    padding: 20px 22px;
    font-family: "Lato", sans-serif;
  }
  .card__brand {
    display: flex;
    align-items: center;
    gap: 10px;
    font-family: "Cinzel", serif;
    font-weight: 600;
    color: #ffffff;
  }
  .card__brand .brand-square {
    width: 30px;
    height: 30px;
    background: #ffffff;
  }
  .card__brand .brand-name { display: block; font-size: 20px; line-height: 1; }
  .card__brand .brand-sub { display: block; font-size: 11px; margin-top: 3px; font-weight: 400; }
  .card__person {
    position: absolute;
    left: 22px;
    top: 100px;
  }
  .card__name {
    font-family: "Cinzel", serif;
    font-size: 13px;
    color: #ffffff;
  }
  .card__title { font-size: 9px; margin-top: 2px; }
  .card__address { font-size: 9.5px; line-height: 1.35; margin-top: 12px; }
  .card__contacts {
    position: absolute;
    right: 22px;
    top: 82px;
    text-align: right;
    font-size: 8.5px;
    line-height: 1.45;
  }
  .card__contacts .label { font-size: 6.5px; letter-spacing: 0.5px; text-transform: uppercase; opacity: 0.8; }
  .card__contacts .gap { height: 8px; }
</style>
</head>
<body>
<main class="canvas">

  <section class="folder" aria-label="Presentation folder and form sheet">
    <div class="folder__corner"><span class="brand-square"></span></div>
  </section>

  <section class="letterhead" aria-label="Letterhead">
    <div class="letterhead__brand">
      <span class="brand-square"></span>
      <span class="brand-name">Kestrel</span>
      <span class="brand-sub">Trust Services</span>
    </div>
    <div class="letterhead__watermark" aria-hidden="true">KESTREL</div>
    <div class="letterhead__footer">88 Harbour Crest Road &bull; Westbridge, Northshire, 40219 &bull; 310-555-0148 &bull; www.kestreltrust.com</div>
  </section>

  <section class="card card--back" aria-label="Business card back">
    <span class="brand-square"></span>
    <span class="brand-name">KESTREL</span>
    <div class="card__web">WWW.KESTRELTRUST.COM</div>
  </section>

  <section class="card card--front" aria-label="Business card front">
    <div class="card__brand">
      <span class="brand-square"></span>
      <div>
        <span class="brand-name">KESTREL</span>
        <span class="brand-sub">Trust Services</span>
      </div>
    </div>
    <div class="card__person">
      <div class="card__name">Daniel Hartley</div>
      <div class="card__title">Director of Operations</div>
      <div class="card__address">88 Harbour Crest Road<br>Westbridge, Northshire, 40219</div>
    </div>
    <div class="card__contacts">
      <div><span class="label">office</span> 310-555-0148</div>
      <div><span class="label">cel</span> 310-555-0192</div>
      <div><span class="label">skype</span> d.hartley.ks</div>
      <div><span class="label">wickr</span> d.hartley.kestrel</div>
      <div class="gap"></div>
      <div>daniel@kestreltrust.com</div>
      <div>www.kestreltrust.com</div>
    </div>
  </section>

</main>
</body>
</html>
```